needs to stand out, but be very clean
Project: Logo for auto broker stationary,
Logo for auto broker stationary,  - Automotive
Logo for auto broker stationary,
Professional
Harbor Motorworks USA
Los Angeles based, Global shipping
Dorian@harbormotorworks-example.com
www.harbormotorworks-example.com
I would like to have at least one file in vector eps, logo and cards. I would like 4 or 6 automotive logos in the corners (4) velorian, Kastra, Tenko, Ardello or (6) Velorian, Kastra, Ardello, Tenko, Ardello, Quellano the other two in the middle of top and bottom. If you like the initials HMU you can use them. working on getting 800 number now, please just put in 555-014-2731 and we can change it later. I was thinking black background for card with white or silver writing and maybe some kind of splash of red.
Pick a font or style you like saying: You don't go to court without an attorney. Why would you buy a car without your Broker?
DorianPlume DorianPlume
I'm surprised that only one person actually read what I wrote and showed me one business card with car logos (kastra, velorian etc. ) on it. I think I like the logo centered.

```html
<!DOCTYPE html>
<html lang="en">
<head>
<meta charset="utf-8">
<title>Harbor Motorworks USA – Business Cards</title>
<link rel="stylesheet" href="https://fonts.googleapis.com/css2?family=Cinzel:wght@600&family=Arimo:wght@400&display=swap">
<style>
  :root{
    --bg:#e4e2de;
    --card:#0d0d0d;
    --card-top:#1c1c1c;
    --red:#e3151b;
    --red-dark:#9e0b10;
    --silver:#c9c9c9;
    --text:#e8e8e8;
    --muted:#bdbdbd;
    --rule:#5a5a5a;
  }
  *{margin:0;padding:0;box-sizing:border-box}
  html,body{width:1200px;height:852px;overflow:hidden;background:var(--bg)}
  .stage{position:relative;width:1200px;height:852px}
  .card{
    position:absolute;width:520px;height:300px;border-radius:16px;overflow:hidden;
    background:linear-gradient(160deg,var(--card-top) 0%,var(--card) 55%);
    box-shadow:0 6px 18px rgba(0,0,0,.25);
    font-family:"Arimo",Arial,sans-serif;color:var(--text);
  }
  .card--left{left:90px;top:80px}
  .card--right{left:590px;top:470px}
  .swoosh{position:absolute;left:0;bottom:0;width:520px;height:120px}
  .brand{display:flex;align-items:center;gap:10px;position:absolute}
  .brand-dot{width:12px;height:12px;border-radius:50%;background:var(--red);flex:none}
  .brand-name{font-family:"Cinzel",Georgia,serif;font-weight:600;color:#fff;letter-spacing:1px;line-height:1.15}
  .card--left .brand{left:32px;top:108px;width:270px}
  .card--left .brand-name{font-size:21px}
  .divider{position:absolute;width:1px;background:var(--rule)}
  .card--left .divider{left:302px;top:28px;height:160px}
  .person-name{font-family:"Cinzel",Georgia,serif;font-weight:600;color:var(--red);font-size:15px;letter-spacing:1px}
  .person-role{font-size:10.5px;color:var(--text);margin-top:2px}
  .person-base{font-size:9.5px;color:var(--muted);margin-top:14px;line-height:1.4}
  .contacts{list-style:none;font-size:9.5px;color:var(--text)}
  .contacts li{display:flex;align-items:center;gap:7px;height:15px}
  .contacts svg{width:10px;height:10px;flex:none;fill:var(--red)}
  .card--left .identity{position:absolute;left:316px;top:28px}
  .card--left .contacts{position:absolute;left:316px;top:116px}
  .card--right .brand{left:96px;top:36px;width:380px;justify-content:center}
  .card--right .brand-name{font-size:24px}
  .card--right .identity{position:absolute;left:56px;top:112px;width:180px;text-align:right}
  .card--right .divider{left:254px;top:108px;height:92px}
  .card--right .contacts{position:absolute;left:268px;top:112px}
</style>
</head>
<body>
<main class="stage">

  <section class="card card--left" aria-label="Business card, side-by-side layout">
    <svg class="swoosh" viewBox="0 0 520 120" preserveAspectRatio="none" aria-hidden="true">
      <path d="M0 78 C160 70 340 40 520 4 L520 18 C340 54 160 84 0 92 Z" fill="var(--silver)"/>
      <path d="M0 92 C160 84 340 54 520 18 L520 120 L0 120 Z" fill="var(--red)"/>
      <path d="M0 104 C180 98 360 72 520 40 L520 120 L0 120 Z" fill="var(--red-dark)" opacity=".35"/>
    </svg>
    <div class="brand"><span class="brand-dot"></span><span class="brand-name">Harbor Motorworks USA</span></div>
    <div class="divider"></div>
    <div class="identity">
      <div class="person-name">DORIAN PLUME</div>
      <div class="person-role">Managing Director</div>
      <div class="person-base">Los Angeles based<br>Global shipping</div>
    </div>
    <ul class="contacts">
      <li><svg viewBox="0 0 10 10"><path d="M2 0 L4 2.5 L3 3.6 Q4.2 5.8 6.4 7 L7.5 6 L10 8 L8.6 10 Q3 9.6 0 1.4 Z"/></svg>1 800 555 0199(T)</li>
      <li><svg viewBox="0 0 10 10"><path d="M2.5 0 H7.5 V10 H2.5 Z M3.5 1 V8 H6.5 V1 Z"/></svg>555-014-2731</li>
      <li><svg viewBox="0 0 10 10"><path d="M0 2 H10 V8 H0 Z M0.8 2.6 L5 5.6 L9.2 2.6 V3.4 L5 6.4 L0.8 3.4 Z" fill-rule="evenodd"/></svg>Dorian@harbormotorworks-example.com</li>
      <li><svg viewBox="0 0 10 10"><path d="M5 0 A5 5 0 1 0 5.01 0 Z M5 1.2 A3.8 3.8 0 1 1 4.99 1.2 Z M1 4.6 H9 V5.4 H1 Z M4.6 1 H5.4 V9 H4.6 Z" fill-rule="evenodd"/></svg>www.harbormotorworks-example.com</li>
    </ul>
  </section>

  <section class="card card--right" aria-label="Business card, centered brand layout">
    <svg class="swoosh" viewBox="0 0 520 120" preserveAspectRatio="none" aria-hidden="true">
      <path d="M0 78 C160 70 340 40 520 4 L520 18 C340 54 160 84 0 92 Z" fill="var(--silver)"/>
      <path d="M0 92 C160 84 340 54 520 18 L520 120 L0 120 Z" fill="var(--red)"/>
      <path d="M0 104 C180 98 360 72 520 40 L520 120 L0 120 Z" fill="var(--red-dark)" opacity=".35"/>
    </svg>
    <div class="brand"><span class="brand-dot"></span><span class="brand-name">Harbor Motorworks USA</span></div>
    <div class="identity">
      <div class="person-name">DORIAN PLUME</div>
      <div class="person-role">Managing Director</div>
      <div class="person-base">Los Angeles based<br>Global shipping</div>
    </div>
    <div class="divider"></div>
    <ul class="contacts">
      <li><svg viewBox="0 0 10 10"><path d="M2 0 L4 2.5 L3 3.6 Q4.2 5.8 6.4 7 L7.5 6 L10 8 L8.6 10 Q3 9.6 0 1.4 Z"/></svg>1 800 555 0199(T)</li>
      <li><svg viewBox="0 0 10 10"><path d="M2.5 0 H7.5 V10 H2.5 Z M3.5 1 V8 H6.5 V1 Z"/></svg>555-014-2731</li>
      <li><svg viewBox="0 0 10 10"><path d="M0 2 H10 V8 H0 Z M0.8 2.6 L5 5.6 L9.2 2.6 V3.4 L5 6.4 L0.8 3.4 Z" fill-rule="evenodd"/></svg>Dorian@harbormotorworks-example.com</li>
      <li><svg viewBox="0 0 10 10"><path d="M5 0 A5 5 0 1 0 5.01 0 Z M5 1.2 A3.8 3.8 0 1 1 4.99 1.2 Z M1 4.6 H9 V5.4 H1 Z M4.6 1 H5.4 V9 H4.6 Z" fill-rule="evenodd"/></svg>www.harbormotorworks-example.com</li>
    </ul>
  </section>

</main>
</body>
</html>
```